Letterhead needed using basic elements of our new logo!

We have just had a new logo and business card created on Pixel Harbor and now would like a new letterhead for our company re-branding. Our logo inspires trust, professionalism and confidence and we would like to mirror that in our letterhead. We would like to use elements in our logo (as well as the logo itself, obviously), but understand with only a header and the ability to print in black and white, we are somewhat limited. We have also won the Resident's Pick Medal for best Property Management Company in our city and would like to somehow include that small banner (see uploaded file) in the letterhead, without it clashing?

Text to include:
Bright Cove Property Management (and logo)
C-214 Tamblyn Cres, Winnipeg, MB R2K 3P7
Ph: 204-739-8152
Fax: 1-888-376-2914
Email: customerservice@brightcovepropertymanagement.example
Web: www.brightcovepropertymanagement.example

Pasted below is our mission, vision and branding statements to help with the project:

Mission Statement

Provide the highest quality customer service to both property owners and tenants using innovative technology and well trained, caring staff.

Vision Statement

To redefine the way in which management is delivered to its customers, becoming the recognized leader in the property management industry.

Brand Essence

When our customers experience our product or service, it brings forth an emotion of absolute trust that we have their best interests at heart

Brand Personality

We are a company that is passionate about our customers, our company and our vision to be leaders in the field of property management. We are visionaries that aren't afraid to use cutting edge technologies to improve our products and service.

Position or Value Proposition

To whom are we speaking?
- real estate investors, including first timers that are giving us their first starter home. They are fairly naive, as they are not "big time" investors, and because they are giving us their first home (in contract to an investor buying a rental property, often sight unseen) they are more emotionally tied to their property and will require a company that inspires trust and confidence.

What is our brand promise?
- we will do our best to serve our clients, both owners and tenants, to give them prompt communication, clear, concise answers to their questions, and look after their property quickly and competently.

Why is our product different than the competition and why should our customers care?
- the current model used by most management companies employs individual portfolio managers that do things a little differently each instance, and differently than their fellow staff members. Our management product is superior because we use a combination of technology and strict procedures to ensure each client's experience is consistent, each and every time.

Industry/Entity Type

Business

Requirements
Must have
• We would like an option to be in black and white, to be able to be printed from Microsoft Word. As well, we do not want anything in a footer or any other kind of letterhead that bleeds below a header. The main use of this letterhead will be from our property management software, to be used in our form letters and other templates (sent to tenants and clients)
Should not have
• Footer or other elements where the text body would be, it will be used in a form letter

```html
<!DOCTYPE html>
<html lang="en">
<head>
<meta charset="utf-8">
<title>Bright Cove Property Management – Letterhead</title>
<link rel="stylesheet" href="https://fonts.googleapis.com/css2?family=Roboto:wght@400;500;700&display=swap">
<style>
  :root {
    --backdrop: #e6e6e6;
    --paper: #f2f2f2;
    --brand-blue: #1b8fd2;
    --ink: #4a4a4a;
    --mark-dark: #3a3a3c;
    --rule: #8a8a8a;
  }
  html, body {
    margin: 0;
    padding: 0;
    width: 1024px;
    height: 1200px;
    overflow: hidden;
    background: var(--backdrop);
    font-family: "Roboto", Arial, sans-serif;
  }
  .letterhead {
    position: absolute;
    left: 72px;
    top: 30px;
    width: 881px;
    height: 1140px;
    background: var(--paper);
    box-shadow: 0 2px 10px rgba(0,0,0,0.12);
  }
  .letterhead__header {
    position: absolute;
    left: 78px;
    right: 87px;
    top: 108px;
  }
  .brand {
    display: flex;
    align-items: center;
    gap: 12px;
    height: 52px;
  }
  .brand__square {
    width: 40px;
    height: 40px;
    background: var(--mark-dark);
  }
  .brand__name {
    font-size: 24px;
    font-weight: 700;
    color: var(--brand-blue);
    letter-spacing: 0.3px;
  }
  .contact {
    margin-top: 24px;
    font-size: 12.5px;
    color: var(--ink);
    line-height: 19px;
  }
  .contact__label {
    color: var(--brand-blue);
    font-weight: 700;
  }
  .contact__item { margin-right: 8px; }
  .header-rule {
    margin: 5px 0 0;
    border: 0;
    border-top: 1px solid var(--rule);
  }
  .website {
    margin-top: 6px;
    font-size: 12px;
    color: var(--brand-blue);
  }
</style>
</head>
<body>
  <main class="letterhead">
    <header class="letterhead__header">
      <div class="brand">
        <span class="brand__square"></span>
        <span class="brand__name">Bright Cove Property Management</span>
      </div>
      <div class="contact">
        <div class="contact__address">C-214 Tamblyn Cres, Winnipeg, MB R2K 3P7</div>
        <div class="contact__lines">
          <span class="contact__item"><span class="contact__label">P:</span> 204-739-8167</span>
          <span class="contact__item"><span class="contact__label">M:</span> 204-739-8152</span>
          <span class="contact__item"><span class="contact__label">F:</span> 1-888-376-2914</span>
          <span class="contact__item"><span class="contact__label">E:</span> alex.marsh@brightcovepropertymanagement.example</span>
        </div>
      </div>
      <hr class="header-rule">
      <div class="website">www.brightcovepropertymanagement.example</div>
    </header>
  </main>
</body>
</html>
```